Whitmore Business Card Design

The name of the business is Dara Whitmore, CPA LLC
The service that we offer is Accounting, Tax & Consulting Services. I need it to have the following items:
Dara Whitmore, Principal
Phone Number
Email Address
Physical Address

I have attached the company logo, one in black and one in white. Please provide a design in black background and the other in white background. Please include "Accounting, Tax & Consulting Services". I want the business card to be clean and very professional.

```html
<!DOCTYPE html>
<html lang="en">
<head>
<meta charset="utf-8">
<title>Dara Whitmore, CPA LLC — Business Cards</title>
<link href="https://fonts.googleapis.com/css2?family=Montserrat:wght@500;600;700&family=Open+Sans:wght@400&display=swap" rel="stylesheet">
<style>
  :root {
    --backdrop: #dcdddc;
    --paper: #ffffff;
    --ink: #2b2b2d;
    --charcoal: #333335;
    --accent: #9e1a1d;
    --muted: #7a7a7c;
  }
  * { box-sizing: border-box; margin: 0; padding: 0; }
  html, body { width: 1200px; height: 800px; overflow: hidden; }
  body { background: var(--backdrop); position: relative; font-family: "Open Sans", sans-serif; color: var(--ink); }

  .card {
    position: absolute;
    width: 431px; height: 272px;
    background: var(--paper);
    box-shadow: 0 2px 6px rgba(0,0,0,.18);
    overflow: hidden;
  }
  .card--back { left: 193px; top: 102px; }
  .card--front { left: 567px; top: 424px; }

  /* wordmark */
  .wordmark { position: absolute; display: flex; align-items: center; }
  .wordmark__square { background: var(--accent); flex: none; }
  .wordmark__name { font-family: "Montserrat", sans-serif; font-weight: 600; color: var(--ink); white-space: nowrap; line-height: 1; }
  .wordmark__sub { font-family: "Montserrat", sans-serif; font-weight: 600; color: var(--muted); white-space: nowrap; line-height: 1; }

  .card--back .wordmark { left: 33px; top: 49px; gap: 8px; }
  .card--back .wordmark__square { width: 20px; height: 20px; }
  .card--back .wordmark__name { font-size: 11px; }
  .card--back .wordmark__sub { font-size: 7px; letter-spacing: 1.1px; margin-top: 3px; }

  .contact { position: absolute; left: 33px; font-size: 7.6px; line-height: 14px; }
  .contact--address { top: 121px; }
  .contact--lines { top: 171px; }

  .person { position: absolute; left: 262px; top: 168px; }
  .person__name { font-size: 15.5px; letter-spacing: 1px; line-height: 1; color: var(--ink); }
  .person__rule { width: 19px; height: 1px; background: var(--accent); margin: 5px 0 6px; }
  .person__role { font-size: 9.5px; letter-spacing: 1px; color: var(--muted); line-height: 1; }

  .footer-bar { position: absolute; background: var(--charcoal); }
  .footer-square { position: absolute; background: var(--accent); }
  .card--back .footer-bar { left: 0; bottom: 0; width: 399px; height: 12px; }
  .card--back .footer-square { right: 0; bottom: 0; width: 12px; height: 12px; }
  .footer-bar__text { position: absolute; left: 33px; top: 3px; font-family: "Montserrat", sans-serif; font-weight: 500; font-size: 5.3px; letter-spacing: .5px; color: #fff; white-space: nowrap; }

  .card--front .wordmark { left: 69px; top: 107px; gap: 13px; }
  .card--front .wordmark__square { width: 36px; height: 36px; }
  .card--front .wordmark__name { font-size: 17.5px; }
  .card--front .wordmark__sub { font-size: 11.5px; letter-spacing: 1.4px; margin-top: 4px; }
  .front__rule { position: absolute; left: 64px; top: 151px; width: 309px; height: 1px; background: var(--ink); }
  .front__tagline { position: absolute; left: 64px; width: 309px; top: 157px; text-align: center; font-family: "Montserrat", sans-serif; font-weight: 500; font-size: 8.4px; letter-spacing: 3.2px; color: var(--muted); white-space: nowrap; }
  .card--front .footer-square { left: 0; bottom: 0; width: 13px; height: 14px; }
  .card--front .footer-bar { left: 34px; right: 0; bottom: 0; height: 14px; }
</style>
</head>
<body>
  <section class="card card--back" aria-label="Business card, contact side">
    <div class="wordmark">
      <span class="wordmark__square"></span>
      <div>
        <div class="wordmark__name">Dara Whitmore, CPA LLC</div>
        <div class="wordmark__sub">CERTIFIED PUBLIC ACCOUNTANT</div>
      </div>
    </div>
    <p class="contact contact--address">Company address line 1<br>Address line 2</p>
    <p class="contact contact--lines">+1 555 014 2290<br>dara@whitmorecpa.com<br>www.whitmorecpa.com</p>
    <div class="person">
      <div class="person__name">DARA WHITMORE</div>
      <div class="person__rule"></div>
      <div class="person__role">PRINCIPAL</div>
    </div>
    <div class="footer-bar"><span class="footer-bar__text">ACCOUNTING | TAX | CONSULTING SERVICES</span></div>
    <div class="footer-square"></div>
  </section>

  <section class="card card--front" aria-label="Business card, brand side">
    <div class="wordmark">
      <span class="wordmark__square"></span>
      <div>
        <div class="wordmark__name">Dara Whitmore, CPA LLC</div>
        <div class="wordmark__sub">CERTIFIED PUBLIC ACCOUNTANT</div>
      </div>
    </div>
    <div class="front__rule"></div>
    <div class="front__tagline">ACCOUNTING | TAX | CONSULTING SERVICES</div>
    <div class="footer-square"></div>
    <div class="footer-bar"></div>
  </section>
</body>
</html>
```